Create Label for Jojoba Oil and Argan Oil

We already have a logo design and we tried editing a label for pure Jojoba and Argan oils. We would like to have someone do two designs for our label.

We want people to distinguish between the two bottles of Argan and Jojoba but they must be on the same theme.

Also, we would like to have an elegant feel to the label.

Logo Design is attached in the files and some pictures of the bottles. The current labels are just their because we tried coming up with our own labels. You have freedom to change the look.

Target Market(s)

adult women and men

Industry/Entity Type

Cosmetic

Requirements
Must have
• The container uses Frosted glass as shown in pictures attached.
• Please do not change the shape of the Logo; although you have freedom to change the color.
• Designs must contain the following:
• For our Jojoba Oil:
• -- 100% Pure Jojoba Oil
• -- Face, Body & Hair
• -- 118 mL
• -- www.varolune.com
• -- Ingredient: Simmondsia Chinensis (Jojoba) Seed Oil
• -- For external use only
• -- must fit within 3" X 2.5" HIGH-GLOSS PAPER
• For our Argan Oil:
• -- 100% Pure Moroccan Argan Oil
• -- Face, Body & Hair
• -- 50 mL
• -- www.varolune.com
• -- Ingredient: Argania Spinosa (Argan) Kernel Oil
• -- must fit within 3.25" X 1.75" HIGH-GLOSS PAPER
Nice to have
• Must be good printed on High Gloss Paper and seen on a Website.

```html
<!DOCTYPE html>
<html lang="en">
<head>
<meta charset="utf-8">
<title>Varolune Oil Labels</title>
<link href="https://fonts.googleapis.com/css2?family=Raleway:wght@400;500&family=Montserrat:wght@400;500;600&family=Great+Vibes&display=swap" rel="stylesheet">
<style>
  :root {
    --canvas: #e5e5e5;
    --paper: #ffffff;
    --ink: #1a1a1a;
    --jojoba: #3fa62e;
    --argan: #ff7f00;
    --rule: #888888;
  }
  * { margin: 0; padding: 0; box-sizing: border-box; }
  html, body { width: 1200px; height: 1200px; overflow: hidden; }
  body {
    background: var(--canvas);
    position: relative;
    font-family: "Montserrat", sans-serif;
    color: var(--ink);
  }
  .dimension { position: absolute; font-size: 11px; font-weight: 600; }
  .dimension-width { left: 426px; top: 155px; }
  .dimension-height { left: 231px; top: 392px; }
  .dimension-lines { position: absolute; left: 0; top: 0; }

  /* Jojoba label: 2.5in x 3in */
  .label {
    position: absolute;
    width: 309px;
    height: 370px;
    background: var(--paper);
    overflow: hidden;
    --accent: var(--jojoba);
  }
  .label--rounded { border-radius: 17px; }
  .label--jojoba.row-top { left: 283px; top: 205px; }
  .label--jojoba.row-bottom { left: 283px; top: 630px; }

  /* Argan label: 1.75in x 3.25in */
  .label--argan { --accent: var(--argan); width: 216px; height: 402px; }
  .label--argan.row-top { left: 664px; top: 189px; }
  .label--argan.row-bottom { left: 664px; top: 614px; }

  .brand-mark {
    position: absolute; left: 129px; top: 13px;
    width: 50px; height: 50px; border-radius: 50%;
    border: 3px solid var(--accent);
  }
  .brand-name {
    position: absolute; left: 0; width: 100%; top: 64px;
    text-align: center; font-family: "Raleway", sans-serif; font-weight: 400;
    font-size: 34px; line-height: 40px; color: var(--accent); letter-spacing: 0.3px;
  }
  .purity-badge {
    position: absolute; left: 95px; top: 107px; width: 119px; height: 26px;
    background: var(--accent); color: #fff;
    display: flex; align-items: center; justify-content: center; gap: 4px;
    font-family: "Raleway", sans-serif; font-size: 19px; font-weight: 500; line-height: 1;
  }
  .purity-badge .script { font-family: "Great Vibes", cursive; font-size: 22px; font-weight: 400; }
  .origin {
    position: absolute; left: 0; width: 100%; top: 137px; text-align: center;
    font-size: 9px; letter-spacing: 2px; line-height: 11px;
  }
  .product-name {
    position: absolute; left: 0; width: 100%; top: 140px; text-align: center;
    font-family: "Great Vibes", cursive; font-size: 48px; line-height: 52px; white-space: nowrap;
  }
  .use-area {
    position: absolute; left: 0; width: 100%; top: 196px; text-align: center;
    font-size: 10px; line-height: 12px; letter-spacing: 0.6px;
  }
  .divider { position: absolute; left: 94px; width: 121px; top: 211px; height: 1px; background: var(--rule); }
  .caution {
    position: absolute; left: 0; width: 100%; top: 216px; text-align: center;
    font-size: 12px; line-height: 15px; letter-spacing: 0.6px;
  }
  .botanical { position: absolute; left: 80px; top: 236px; width: 140px; height: 88px; }
  .origin-city { position: absolute; left: 59px; top: 332px; font-size: 11px; line-height: 13px; }
  .volume { position: absolute; right: 34px; top: 326px; font-size: 17px; line-height: 20px; font-family: "Raleway", sans-serif; }
  .ingredient {
    position: absolute; left: 284px; top: 344px; width: 260px;
    transform: rotate(-90deg); transform-origin: 0 0;
    font-size: 9.5px; line-height: 12px; white-space: nowrap; text-align: center;
  }
  .web-band {
    position: absolute; left: 0; bottom: 0; width: 100%; height: 20px;
    background: var(--accent); color: #fff;
    display: flex; align-items: center; justify-content: center;
    font-size: 11px; font-weight: 600; letter-spacing: 1px;
  }

  /* Argan positions within the narrower label */
  .label--argan .brand-mark { left: 75px; top: 16px; }
  .label--argan .brand-name { left: 0; width: 196px; top: 72px; font-size: 32px; }
  .label--argan .purity-badge { left: 39px; top: 114px; }
  .label--argan .origin { width: 196px; top: 148px; }
  .label--argan .product-name { width: 196px; top: 160px; font-size: 42px; line-height: 46px; }
  .label--argan .use-area { width: 196px; top: 214px; }
  .label--argan .divider { left: 40px; width: 116px; top: 229px; }
  .label--argan .caution { width: 196px; top: 234px; font-size: 11.5px; }
  .label--argan .botanical { left: 28px; top: 256px; width: 140px; height: 96px; }
  .label--argan .origin-city { left: 14px; top: 364px; }
  .label--argan .volume { right: 26px; top: 358px; }
  .label--argan .ingredient { left: 196px; top: 376px; width: 340px; }
</style>
</head>
<body>
  <svg class="dimension-lines" width="1200" height="1200" aria-hidden="true">
    <g stroke="#222" stroke-width="1" fill="#222">
      <line x1="285" y1="178" x2="589" y2="178"/>
      <polygon points="283,178 290,175 290,181"/>
      <polygon points="591,178 584,175 584,181"/>
      <line x1="256" y1="207" x2="256" y2="573"/>
      <polygon points="256,205 253,212 259,212"/>
      <polygon points="256,575 253,568 259,568"/>
    </g>
  </svg>
  <div class="dimension dimension-width">2.5″</div>
  <div class="dimension dimension-height">3″</div>

  <section class="label label--jojoba row-top">
    <div class="brand-mark"></div>
    <div class="brand-name">Varolune</div>
    <div class="purity-badge">100% <span class="script">Pure</span></div>
    <div class="product-name">Jojoba Oil</div>
    <div class="use-area">Face, Body &amp; Hair</div>
    <div class="divider"></div>
    <div class="caution">For external use only</div>
    <svg class="botanical" role="img" aria-label="Illustration of a jojoba branch with seed pods and leaves"><defs><linearGradient id="g1" x1="0" y1="0" x2="1" y2="1"><stop offset="0" stop-color="#e8f2e4"/><stop offset="1" stop-color="#8cc47c"/></linearGradient></defs><rect width="140" height="88" rx="10" fill="url(#g1)"/></svg>
    <div class="origin-city">Chicago IL</div>
    <div class="volume">118 mL</div>
    <div class="ingredient">Ingredient: Simmondsia Chinensis (Jojoba) Seed Oil</div>
    <div class="web-band">www. varolune.com</div>
  </section>

  <section class="label label--argan row-top">
    <div class="brand-mark"></div>
    <div class="brand-name">Varolune</div>
    <div class="purity-badge">100% <span class="script">Pure</span></div>
    <div class="origin">MOROCCAN</div>
    <div class="product-name">Argan Oil</div>
    <div class="use-area">Face, Body &amp; Hair</div>
    <div class="divider"></div>
    <div class="caution">For external use only</div>
    <svg class="botanical" role="img" aria-label="Illustration of an argan branch with fruits and leaves"><defs><linearGradient id="g2" x1="0" y1="0" x2="1" y2="1"><stop offset="0" stop-color="#eef4ea"/><stop offset="1" stop-color="#86c070"/></linearGradient></defs><rect width="140" height="96" rx="10" fill="url(#g2)"/></svg>
    <div class="origin-city">Chicago IL</div>
    <div class="volume">50 mL</div>
    <div class="ingredient">Ingredient: Argania Spinosa (Argan) Kernel Oil</div>
    <div class="web-band">www. varolune.com</div>
  </section>

  <section class="label label--jojoba label--rounded row-bottom">
    <div class="brand-mark"></div>
    <div class="brand-name">Varolune</div>
    <div class="purity-badge">100% <span class="script">Pure</span></div>
    <div class="product-name">Jojoba Oil</div>
    <div class="use-area">Face, Body &amp; Hair</div>
    <div class="divider"></div>
    <div class="caution">For external use only</div>
    <svg class="botanical" role="img" aria-label="Illustration of a jojoba branch with seed pods and leaves"><defs><linearGradient id="g3" x1="0" y1="0" x2="1" y2="1"><stop offset="0" stop-color="#e8f2e4"/><stop offset="1" stop-color="#8cc47c"/></linearGradient></defs><rect width="140" height="88" rx="10" fill="url(#g3)"/></svg>
    <div class="origin-city">Chicago IL</div>
    <div class="volume">118 mL</div>
    <div class="ingredient">Ingredient: Simmondsia Chinensis (Jojoba) Seed Oil</div>
    <div class="web-band">www. varolune.com</div>
  </section>

  <section class="label label--argan label--rounded row-bottom">
    <div class="brand-mark"></div>
    <div class="brand-name">Varolune</div>
    <div class="purity-badge">100% <span class="script">Pure</span></div>
    <div class="origin">MOROCCAN</div>
    <div class="product-name">Argan Oil</div>
    <div class="use-area">Face, Body &amp; Hair</div>
    <div class="divider"></div>
    <div class="caution">For external use only</div>
    <svg class="botanical" role="img" aria-label="Illustration of an argan branch with fruits and leaves"><defs><linearGradient id="g4" x1="0" y1="0" x2="1" y2="1"><stop offset="0" stop-color="#eef4ea"/><stop offset="1" stop-color="#86c070"/></linearGradient></defs><rect width="140" height="96" rx="10" fill="url(#g4)"/></svg>
    <div class="origin-city">Chicago IL</div>
    <div class="volume">50 mL</div>
    <div class="ingredient">Ingredient: Argania Spinosa (Argan) Kernel Oil</div>
    <div class="web-band">www. varolune.com</div>
  </section>
</body>
</html>
```